EmberDepot, Charcoal bag packaging and brand

I'm looking at a package design for 10 KG/22 pounds of charcoal.
The design must include a name that is catchy and conveys quality, heat and low ash. The name must not violate any trademarks or tradenames. One of the best resources to view other packaging is the Quiet Pelican website. www.quietpelican.com
Two colors only and one must be red which will be printed on a kraft paper bag. The name EMBERDEPOT.COM must be prominent and also list our website of www.emberdepot.com.
Updates
Here is some wording for the front of the bag and it can be in any order. Make it look GREAT! Use the name "Blazewood Charcoal", but the Emberdepot logo should be the most prominant. Hi Heat, Low Ash, Long burning We will need some wording on the back and sides, but it's primarily just text and we won't worry about it until later. A UPC code will be necessary also. Thanks, Rick Tolben
100% Natural Hardwood Lump Charcoal
Restaurant and Competition grade
No additives, No fillers
Non sparking
Easy lighting, use a chimney starter
Mild flavor profile
A number of the designs are using full coverage ink.
Please limit the amount of ink coverage to no more than 25% ..
It becomes very costly to use 100% coverage.
Thanks!
Rick Tolben
Thank you to all the fine designers.
It was an extremely difficult decision for us. One fine designer was knocked out of the competition by our attorneys and we also received notice from the same attorneys that our brand of "Blazewood Charcoal" won't work...
I'll be posting another new logo design for branding of the charcoal at some point.
Kindest regards to all.
Rick Tolben
Target Market(s)
End users, restaurants, resorts, competition cookoffs
Look and feel
Each slider illustrates characteristics of the customer's brand and the style your logo design should communicate.

```html
<!DOCTYPE html>
<html lang="en">
<head>
<meta charset="utf-8">
<title>Blazewood Hardwood Lump Charcoal – Bag Front</title>
<link rel="stylesheet" href="https://fonts.googleapis.com/css2?family=Open+Sans:wght@800&family=Oswald:wght@600&family=Roboto+Condensed:wght@300&display=swap">
<style>
  :root {
    --backdrop: #e6e7e9;
    --kraft: #dfbd99;
    --kraft-stripe: #c9a680;
    --ink-red: #c8202f;
    --ink-black: #111111;
  }
  html, body {
    margin: 0;
    padding: 0;
    width: 1200px;
    height: 836px;
    overflow: hidden;
    background: var(--backdrop);
  }
  .canvas {
    position: relative;
    width: 1200px;
    height: 836px;
  }
  .bag {
    position: absolute;
    left: 279px;
    top: 0;
    width: 624px;
    height: 836px;
    background-color: var(--kraft);
    background-image: repeating-linear-gradient(90deg,
      transparent 0 24px,
      var(--kraft-stripe) 24px 33px,
      transparent 33px 41px);
    background-position: 8px 0;
  }
  .bag__base-band {
    position: absolute;
    left: 0;
    bottom: 0;
    width: 100%;
    height: 131px;
    background: var(--ink-black);
  }
  .weight-box {
    position: absolute;
    left: 285px;
    top: 123px;
    width: 232px;
    height: 56px;
    border: 1.5px solid var(--ink-black);
    box-sizing: border-box;
    display: flex;
  }
  .weight-box__icon {
    width: 64px;
    border-right: 1.5px solid var(--ink-black);
    display: flex;
    align-items: center;
    justify-content: center;
  }
  .brand-lockup {
    position: absolute;
    left: 0;
    top: 290px;
    width: 624px;
    height: 240px;
    overflow: visible;
  }
  .brand-lockup .brand-name {
    font-family: "Oswald", sans-serif;
    font-weight: 600;
    fill: var(--ink-red);
    letter-spacing: 2px;
  }
  .brand-lockup .product-line {
    font-family: "Open Sans", sans-serif;
    font-weight: 800;
    fill: var(--ink-black);
  }
  .brand-lockup .product-type {
    font-family: "Oswald", sans-serif;
    font-weight: 600;
    fill: var(--ink-red);
  }
  .feature-panel {
    position: absolute;
    left: 100px;
    top: 551px;
    width: 424px;
    height: 76px;
    background: var(--ink-black);
    border-radius: 8px;
    display: grid;
    grid-template-columns: auto auto;
    justify-content: space-between;
    align-content: center;
    padding: 0 14px;
    box-sizing: border-box;
    font-family: "Roboto Condensed", sans-serif;
    font-weight: 300;
    font-size: 23px;
    line-height: 27px;
    color: var(--kraft);
    white-space: nowrap;
  }
  .feature-panel__item:nth-child(even) { text-align: right; }
  .web-address {
    position: absolute;
    left: 0;
    top: 636px;
    width: 624px;
    text-align: center;
    font-family: "Open Sans", sans-serif;
    font-weight: 800;
    font-size: 30px;
    line-height: 40px;
    color: var(--ink-red);
    -webkit-text-stroke: 1.5px var(--ink-black);
    paint-order: stroke fill;
    margin: 0;
  }
</style>
</head>
<body>
<div class="canvas">
  <div class="bag">
    <div class="weight-box">
      <div class="weight-box__icon">
        <svg width="36" height="36" viewBox="0 0 36 36" aria-hidden="true">
          <circle cx="18" cy="18" r="15" fill="none" stroke="#111" stroke-width="1.5"/>
          <line x1="7" y1="7" x2="29" y2="29" stroke="#111" stroke-width="1.5"/>
          <line x1="29" y1="7" x2="7" y2="29" stroke="#111" stroke-width="1.5"/>
        </svg>
      </div>
      <div class="weight-box__field"></div>
    </div>

    <svg class="brand-lockup" viewBox="0 0 624 240" aria-label="Blazewood Hardwood Lump Charcoal">
      <defs>
        <path id="brand-arc" d="M 92 92 Q 312 8 532 92"/>
        <path id="product-arc" d="M 140 128 Q 312 66 484 128"/>
      </defs>
      <text class="brand-name" font-size="62">
        <textPath href="#brand-arc" startOffset="50%" text-anchor="middle" textLength="440" lengthAdjust="spacingAndGlyphs">BLAZEWOOD</textPath>
      </text>
      <text class="product-line" font-size="34">
        <textPath href="#product-arc" startOffset="50%" text-anchor="middle" textLength="338" lengthAdjust="spacingAndGlyphs">Hardwood Lump</textPath>
      </text>
      <text class="product-type" x="312" y="228" text-anchor="middle" font-size="118" textLength="300" lengthAdjust="spacingAndGlyphs">CHARCOAL</text>
    </svg>

    <div class="feature-panel">
      <span class="feature-panel__item">Low Ash</span>
      <span class="feature-panel__item">Consistently High Heat</span>
      <span class="feature-panel__item">Non sparking</span>
      <span class="feature-panel__item">Mild Flavor Profile</span>
    </div>

    <p class="web-address">www.emberdepot.com</p>

    <div class="bag__base-band"></div>
  </div>
</div>
</body>
</html>
```